Business Card Design needed for start up company Pramora

In need of a new business card designed for a start up company based in Sydney, Pramora is a new start up innovative Company, our mission it to make property accessible for everyday Australian and to become the leading Real Estate platform in Australia. We want it to be fresh and clean.

Industry/Entity Type

Financial

Contact Information for Business Card

Section for Name
Section for Title

PRAMORA - Where Doors Open Wide
Mobile:
Direct:

Font styles to use
Sans Serif

Colors
33a6d7
0692cd
0255a3
ffffff

Requirements
Must have
• Logo, all business card details

```html
<!DOCTYPE html>
<html lang="en">
<head>
<meta charset="utf-8">
<title>Pramora Business Card</title>
<link href="https://fonts.googleapis.com/css2?family=Arimo:wght@400;700&display=swap" rel="stylesheet">
<style>
  :root {
    --page-bg: #d4d4d4;
    --white: #ffffff;
    --paper-top: #fbfbfb;
    --paper-bottom: #dcdcdc;
    --blue-deep: #0a6fb4;
    --royal: #0255a3;
    --navy-top: #22477d;
    --navy-bottom: #1a3867;
    --text-soft: #e3f0fa;
  }
  * { box-sizing: border-box; margin: 0; padding: 0; }
  html, body {
    width: 1200px; height: 965px; overflow: hidden;
    background: var(--page-bg);
    font-family: "Arimo", Arial, sans-serif;
  }
  .stage { position: relative; width: 1200px; height: 965px; }
  .card {
    position: absolute; left: 276px; width: 648px; height: 370px;
    border-radius: 44px; overflow: hidden;
  }
  .card-front { top: 96px; background: linear-gradient(180deg, var(--blue-deep), var(--royal)); }
  .card-back { top: 500px; background: linear-gradient(180deg, var(--navy-top), var(--navy-bottom)); }

  .front-brand-panel {
    position: absolute; left: 0; top: 0; width: 341px; height: 100%;
    background: linear-gradient(180deg, var(--paper-top), var(--paper-bottom));
    display: flex; align-items: center; justify-content: center;
  }
  .front-notch { position: absolute; left: 340px; top: 74px; }
  .brand-name {
    font-weight: 400; font-size: 32px; letter-spacing: 6px;
    color: var(--royal);
  }

  .details { position: absolute; left: 397px; top: 70px; color: var(--white); }
  .person-name { font-weight: 700; font-size: 20px; letter-spacing: 0.2px; }
  .person-title { font-weight: 400; font-size: 14px; margin-top: 2px; color: var(--text-soft); }
  .contact-list { list-style: none; margin-top: 48px; font-size: 14px; line-height: 19px; }
  .contact-list li { display: flex; align-items: center; gap: 9px; }
  .contact-list svg { width: 15px; height: 15px; flex: none; }
  .address { margin-top: 36px; font-size: 14px; line-height: 19px; color: var(--text-soft); }

  .back-brand {
    position: absolute; inset: 0;
    display: flex; flex-direction: column; align-items: center; justify-content: center;
    color: var(--white);
  }
  .back-brand .brand-name { font-size: 52px; letter-spacing: 10px; color: var(--white); }
  .tagline { margin-top: 14px; font-size: 18px; letter-spacing: 4px; }
</style>
</head>
<body>
<main class="stage">
  <section class="card card-front" aria-label="Card front">
    <div class="front-brand-panel">
      <span class="brand-name">PRAMORA</span>
    </div>
    <svg class="front-notch" width="20" height="34" viewBox="0 0 20 34"><polygon points="0,0 20,17 0,34" fill="#ececec"/></svg>
    <div class="details">
      <h1 class="person-name">DANIEL HARPER</h1>
      <p class="person-title">Managing Director</p>
      <ul class="contact-list">
        <li><svg viewBox="0 0 16 16" fill="none" stroke="#fff" stroke-width="1.4"><rect x="2" y="2" width="4" height="12"/><rect x="7" y="3" width="7" height="11"/><path d="M9 6h3M9 9h3M9 12h3"/></svg>+61 2 9000 4821</li>
        <li><svg viewBox="0 0 16 16" fill="none" stroke="#fff" stroke-width="1.4"><rect x="4" y="1.5" width="8" height="13" rx="1.5"/><path d="M7 12h2"/></svg>+61 400 118 273</li>
        <li><svg viewBox="0 0 16 16" fill="none" stroke="#fff" stroke-width="1.4"><rect x="1.5" y="3.5" width="13" height="9"/><path d="M1.5 3.5l6.5 5 6.5-5"/></svg>hello@PRAMORA.com.au</li>
        <li><svg viewBox="0 0 16 16" fill="none" stroke="#fff" stroke-width="1.2"><circle cx="8" cy="8" r="6.5"/><ellipse cx="8" cy="8" rx="3" ry="6.5"/><path d="M1.5 8h13M2.5 5h11M2.5 11h11"/></svg>www.PRAMORA.com.au</li>
      </ul>
      <p class="address">Suite 4, 21 Kellett Lane,<br>Paddington, NSW, 2021</p>
    </div>
  </section>

  <section class="card card-back" aria-label="Card back">
    <div class="back-brand">
      <span class="brand-name">PRAMORA</span>
      <p class="tagline">Where Doors Open Wide</p>
    </div>
  </section>
</main>
</body>
</html>
```